Client Fulfillment Flyer

This is a document used for internal purposes ie it is not distributed to clients. We would like it to have some colour, images etc. We are in the financial services industry, Ballarat, Victoria, Australia. www.tarrowfield.com.au and www.tarrowfieldagri.com.au

Target Market(s)

Internal training document

Industry/Entity Type

Finance And Accounting

Colors
3176b5

```html
<!DOCTYPE html>
<html lang="en">
<head>
<meta charset="utf-8">
<title>Tarrowfield &amp; Co — Client Fulfillment Flyer</title>
<link rel="stylesheet" href="https://fonts.googleapis.com/css2?family=Oswald:wght@500;600&family=Roboto:ital,wght@0,400;0,500;0,700;1,500&family=Roboto+Condensed:wght@400&display=swap">
<style>
  :root {
    --brand: #1a5fa8;
    --brand-bright: #3176b5;
    --panel: #cfe6f8;
    --strip: #d3e8f8;
    --ink: #1d3557;
    --paper: #ffffff;
    --backdrop: #eeebe6;
  }
  * { box-sizing: border-box; margin: 0; padding: 0; }
  html, body { width: 1200px; height: 900px; overflow: hidden; background: var(--backdrop); }
  .canvas { position: relative; width: 1200px; height: 900px; overflow: hidden; }
  .flyer {
    position: absolute; left: 311px; top: 20px;
    width: 470px; height: 700px;
    transform: scale(1.2286); transform-origin: top left;
    background: var(--paper); overflow: hidden;
    font-family: "Roboto", sans-serif; color: var(--ink);
    box-shadow: 0 2px 10px rgba(0,0,0,.12);
  }
  .shapes { position: absolute; inset: 0; }
  .brand { position: absolute; left: 13px; top: 18px; display: flex; align-items: center; gap: 9px; }
  .brand-dot { width: 46px; height: 46px; border-radius: 50%; background: var(--brand); }
  .brand-name { font-family: "Oswald", sans-serif; font-weight: 500; font-size: 17px; letter-spacing: 1px; color: var(--brand); }
  .intro { position: absolute; left: 16px; top: 140px; width: 225px; }
  .intro h1 { font-family: "Oswald", sans-serif; font-weight: 600; font-size: 19.5px; line-height: 24.5px; color: var(--brand); }
  .intro p { margin-top: 8px; font-size: 7.6px; line-height: 13px; color: #24364f; }
  .process { position: absolute; left: 16px; top: 332px; width: 230px; }
  .process h2 { font-family: "Oswald", sans-serif; font-weight: 500; font-size: 11px; color: var(--brand); }
  .process .lead { font-size: 6.6px; font-weight: 700; color: var(--brand); margin-top: 3px; }
  .process ul { list-style: none; margin-top: 5px; }
  .process li { font-size: 7.3px; line-height: 14.6px; padding-left: 9px; position: relative; color: #24364f; }
  .process li::before { content: ""; position: absolute; left: 1px; top: 5.5px; width: 4px; height: 4px; border-radius: 50%; background: var(--brand); }
  .services { position: absolute; left: 264px; top: 487px; }
  .services h2 { font-family: "Oswald", sans-serif; font-weight: 600; font-size: 12px; color: var(--brand); }
  .service-list { position: relative; margin-top: 4px; width: 200px; height: 80px; }
  .service { position: absolute; display: flex; align-items: center; gap: 5px; font-family: "Roboto Condensed", sans-serif; font-size: 10px; color: var(--ink); }
  .tick { width: 11px; height: 11px; }
  .contact-title { position: absolute; left: 89px; top: 619px; font-family: "Oswald", sans-serif; font-weight: 600; font-size: 12px; color: var(--brand); }
  .contact-item { position: absolute; top: 646px; font-size: 7.5px; font-style: italic; font-weight: 500; color: var(--brand); text-align: center; line-height: 10.5px; transform: translateX(-50%); white-space: nowrap; }
  .site-strip { position: absolute; left: 0; top: 682px; width: 470px; height: 18px; background: var(--strip); }
  .site-tab { position: absolute; left: 282px; top: 682px; width: 136px; height: 18px; background: var(--brand); clip-path: polygon(8px 0, 100% 0, calc(100% - 8px) 100%, 0 100%); color: #fff; font-size: 7.5px; display: flex; align-items: center; justify-content: center; }
</style>
</head>
<body>
<div class="canvas">
  <div class="flyer">
    <svg class="shapes" width="470" height="700" viewBox="0 0 470 700" aria-hidden="false">
      <defs>
        <linearGradient id="portrait-tone" x1="0" y1="0" x2="1" y2="1">
          <stop offset="0" stop-color="#e8dcd2"/>
          <stop offset="0.5" stop-color="#d9cfc8"/>
          <stop offset="1" stop-color="#9fb6cf"/>
        </linearGradient>
        <linearGradient id="desk-tone" x1="0" y1="0" x2="1" y2="1">
          <stop offset="0" stop-color="#c9ccd1"/>
          <stop offset="1" stop-color="#6f757d"/>
        </linearGradient>
        <linearGradient id="thumb-tone" x1="0" y1="0" x2="0" y2="1">
          <stop offset="0" stop-color="#e9e4de"/>
          <stop offset="1" stop-color="#cfdde8"/>
        </linearGradient>
      </defs>
      <polygon class="hero-photo" role="img" aria-label="Photo of a smiling young man in glasses and a white t-shirt seated with a laptop"
        points="160,108 292,0 470,0 470,305 385,368 95,535 0,535 0,130" fill="url(#portrait-tone)"/>
      <line x1="150" y1="106" x2="287" y2="2" stroke="var(--brand)" stroke-width="5"/>
      <polygon class="intro-panel" points="78,76 256,212 256,388 80,503 4,458 4,132"
        fill="var(--panel)" stroke="var(--brand)" stroke-width="9" stroke-linejoin="round"/>
      <polygon class="accent-band" points="70,582 388,362 392,378 74,598" fill="var(--brand)"/>
      <polygon class="desk-photo" role="img" aria-label="Photo of a laptop on a desk"
        points="470,300 398,348 394,438 470,492" fill="url(#desk-tone)" stroke="var(--brand)" stroke-width="7" stroke-linejoin="round"/>
      <polygon class="thumb-photo" role="img" aria-label="Small photo of a man giving a thumbs up"
        points="4,505 50,530 58,600 4,642" fill="url(#thumb-tone)" stroke="var(--brand)" stroke-width="6" stroke-linejoin="round"/>
      <g class="contact-icons" fill="none" stroke="var(--brand)" stroke-width="1.6">
        <polygon points="220,606 234,614 234,630 220,638 206,630 206,614"/>
        <polygon points="310,606 324,614 324,630 310,638 296,630 296,614"/>
        <polygon points="399,606 413,614 413,630 399,638 385,630 385,614"/>
        <line x1="242" y1="622" x2="289" y2="622" stroke-dasharray="2 3.5" stroke-width="2.2" stroke-linecap="round"/>
        <line x1="331" y1="622" x2="378" y2="622" stroke-dasharray="2 3.5" stroke-width="2.2" stroke-linecap="round"/>
      </g>
      <rect x="215" y="617" width="10" height="10" rx="2" fill="var(--brand)"/>
      <path d="M307 616 q-3 6 0 12 l2 -1 q-2 -5 0 -10 z" fill="var(--brand)"/>
      <rect x="393" y="617.5" width="12" height="9" rx="1" fill="var(--brand)"/>
      <path d="M393.5 618.5 L399 623 L404.5 618.5" fill="none" stroke="#fff" stroke-width="1"/>
    </svg>

    <div class="brand">
      <div class="brand-dot"></div>
      <div class="brand-name">TARROWFIELD &amp; CO</div>
    </div>

    <div class="intro">
      <h1>Hellow<br>We are<br>TARROWFIELD AND CO.</h1>
      <p>We are primarily a service based business however the product we sell is Client Fulfillment. Client Fulfillment in simple terms means providing the services to satisfy client requirements and expectations. Our aim is to not only satisfy but exceed client requirements and expectations. The Client Fulfillment system is the methodology through which we deliver the result we have promised to deliver.</p>
    </div>

    <div class="process">
      <h2>The Client Fulfillment Process</h2>
      <div class="lead">The areas we focus on to deliver Client Fulfillment are:</div>
      <ul>
        <li>Understanding Core Purpose, Core Values, Vision and Why</li>
        <li>Client Management and Communication</li>
        <li>The Basics</li>
        <li>The Are You Financially Secure Process</li>
        <li>The Right People Doing the Right Work</li>
      </ul>
    </div>

    <div class="services">
      <h2>OUR SERVICES AREA</h2>
      <div class="service-list">
        <div class="service" style="left:0;top:6px"><svg class="tick" viewBox="0 0 12 12"><circle cx="6" cy="6" r="6" fill="var(--brand)"/><path d="M3.2 6.2 L5.2 8.1 L8.8 4.2" fill="none" stroke="#fff" stroke-width="1.5"/></svg>Accounting</div>
        <div class="service" style="left:0;top:30px"><svg class="tick" viewBox="0 0 12 12"><circle cx="6" cy="6" r="6" fill="var(--brand)"/><path d="M3.2 6.2 L5.2 8.1 L8.8 4.2" fill="none" stroke="#fff" stroke-width="1.5"/></svg>Financial Planning</div>
        <div class="service" style="left:0;top:54px"><svg class="tick" viewBox="0 0 12 12"><circle cx="6" cy="6" r="6" fill="var(--brand)"/><path d="M3.2 6.2 L5.2 8.1 L8.8 4.2" fill="none" stroke="#fff" stroke-width="1.5"/></svg>Lending</div>
        <div class="service" style="left:107px;top:6px"><svg class="tick" viewBox="0 0 12 12"><circle cx="6" cy="6" r="6" fill="var(--brand)"/><path d="M3.2 6.2 L5.2 8.1 L8.8 4.2" fill="none" stroke="#fff" stroke-width="1.5"/></svg>Legal</div>
        <div class="service" style="left:107px;top:28px"><svg class="tick" viewBox="0 0 12 12"><circle cx="6" cy="6" r="6" fill="var(--brand)"/><path d="M3.2 6.2 L5.2 8.1 L8.8 4.2" fill="none" stroke="#fff" stroke-width="1.5"/></svg>IT</div>
      </div>
    </div>

    <div class="contact-title">CONTRACT US</div>
    <div class="contact-item" style="left:220px">www.social.com/<br>tarrowfieldagrisolutions</div>
    <div class="contact-item" style="left:313px">1300 555 018</div>
    <div class="contact-item" style="left:402px">info@tarrowfieldagri.com.au</div>

    <div class="site-strip"></div>
    <div class="site-tab">https://www.tarrowfield.com.au/</div>
  </div>
</div>
</body>
</html>
```